Design Cover for Catalog and theme pages to match cover design for continuity

I need a catalog cover for our new catalog and have it flow through the pages uniting the design together. Most the hardest work is complete however it needs a designers touch to bring it all together. The attached files include the catalog with products images data and logos. We have more assets however with the 100MB limit we are unable to upload to many more. For additional images you can pull them from our website www.brandowave.example.

Target Market(s)

Tradesmen and trades women who work in the Electrical and Industrial Automation spaces.

Industry/Entity Type

Industrial

Font styles to use
Sans Serif

Colors
3176b5
0555a3
85cae6

Requirements
Must have
• Complete cover design
• Must also have cover theme flow through remaining pages
Nice to have
• Header and Footer on each page
• Index on cover with page reference
Should not have
• This is not a redesign of the whole catalog, please don't drastically change the pages or any of the data in the tables.

```html
<!DOCTYPE html>
<html lang="en">
<head>
<meta charset="UTF-8">
<title>Brandowave Catalog – Cover and Opening Spread</title>
<link rel="stylesheet" href="https://fonts.googleapis.com/css2?family=Montserrat:wght@400;500;600;700&display=swap">
<style>
  :root {
    --backdrop: #eeeeee;
    --paper: #ffffff;
    --brand-sky: #27a3d9;
    --brand-blue: #3176b5;
    --brand-deep: #0555a3;
    --brand-navy: #2b3690;
    --brand-light: #85cae6;
    --ink-navy: #1d3f86;
    --ink-sky: #2aa0d6;
    --ink-dark: #111111;
    --emblem-grey: #d6d6d6;
    --next-page: #5561ad;
  }
  * { box-sizing: border-box; margin: 0; padding: 0; }
  html, body {
    width: 1200px; height: 848px; overflow: hidden;
    background: var(--backdrop);
    font-family: "Montserrat", Arial, sans-serif;
  }
  .canvas { position: relative; width: 1200px; height: 848px; }

  .sheet-header {
    position: absolute; right: 54px; top: 26px; text-align: right;
    font-size: 9px; line-height: 1.35; color: var(--ink-dark);
  }

  .page { position: absolute; top: 198px; height: 440px; }

  /* Opening spread – intro page */
  .intro-page { left: 40px; width: 308px; background: var(--paper); }
  .intro-emblem {
    position: absolute; left: 105px; top: 107px; width: 125px; height: 152px;
    border-radius: 8px;
    background: radial-gradient(ellipse at 50% 50%, var(--emblem-grey) 0%, #ebebeb 60%, var(--paper) 100%);
  }
  .intro-copy {
    position: absolute; left: 128px; top: 298px; width: 174px;
    font-size: 4.6px; line-height: 1.5; color: var(--ink-sky);
  }
  .intro-copy p + p { margin-top: 5px; }
  .intro-copy strong { color: var(--ink-navy); font-weight: 700; }

  /* Opening spread – contents page */
  .contents-page { left: 348px; width: 290px; background: var(--brand-sky); }
  .contents {
    position: absolute; left: 96px; top: 306px; width: 136px;
    color: var(--paper);
  }
  .contents-title { font-size: 4.2px; font-weight: 600; letter-spacing: 0.4px; margin-bottom: 9px; }
  .contents-list { list-style: none; }
  .contents-item {
    display: flex; justify-content: space-between;
    font-size: 4.4px; letter-spacing: 0.2px;
    padding: 2.5px 0 2px; border-bottom: 0.5px solid rgba(255,255,255,0.55);
  }

  /* Cover */
  .cover-page {
    left: 730px; width: 316px;
    background: linear-gradient(180deg, var(--brand-blue) 0%, var(--brand-deep) 45%, var(--brand-navy) 100%);
  }
  .cover-emblem {
    position: absolute; left: 84px; top: 104px; width: 148px; height: 156px;
    border-radius: 10px;
    background: radial-gradient(ellipse at 50% 50%, var(--brand-light) 0%, var(--brand-sky) 45%, rgba(39,163,217,0) 100%);
  }
  .cover-brand {
    position: absolute; left: 0; right: 0; top: 364px;
    display: flex; justify-content: center; align-items: center; gap: 5px;
  }
  .cover-brand-dot { width: 11px; height: 11px; border-radius: 50%; background: var(--brand-light); }
  .cover-brand-name { font-size: 16px; font-weight: 600; color: var(--paper); }
  .cover-tagline {
    position: absolute; left: 0; right: 0; top: 396px; text-align: center;
    font-size: 5px; letter-spacing: 0.6px; color: var(--brand-light);
  }

  /* Following page, cropped at canvas edge */
  .next-page {
    left: 1112px; width: 88px;
    background: linear-gradient(90deg, var(--paper) 0 22px, var(--next-page) 22px);
  }
</style>
</head>
<body>
<main class="canvas">

  <header class="sheet-header">
    <p>P.02</p>
    <p>All rights reserved</p>
  </header>

  <section class="page intro-page">
    <div class="intro-emblem" role="img" aria-label="Large soft grey brand emblem"></div>
    <div class="intro-copy">
      <p><strong>Efficiency through simplicity.</strong> That is our core focus. We help our customers gain efficiency every day with simple, durable products and services designed to maximise productivity with minimal waste of time and effort.</p>
      <p>To build efficiently, we take pride in providing high quality and durable solutions to the market. Our range covers enclosures, controls and system integration in a variety of sizes, colours and materials.</p>
      <p>Founded upon the principle that less is more, we help customers work with simple, efficient and reliable products that respect your time and bring efficiency to daily tasks.</p>
    </div>
  </section>

  <section class="page contents-page">
    <nav class="contents">
      <h2 class="contents-title">CONTENTS</h2>
      <ul class="contents-list">
        <li class="contents-item"><span>ALUMINIUM PROJECT BOXES</span><span>03</span></li>
        <li class="contents-item"><span>LOREM IPSUM DOLOR</span><span>06</span></li>
        <li class="contents-item"><span>DOLOR IPSUM</span><span>07</span></li>
        <li class="contents-item"><span>LOREM IPSUM DOLOR AMET</span><span>09</span></li>
        <li class="contents-item"><span>LOREM IPSUM DOLOR</span><span>11</span></li>
      </ul>
    </nav>
  </section>

  <section class="page cover-page">
    <div class="cover-emblem" role="img" aria-label="Cover brand emblem in light and sky blue"></div>
    <div class="cover-brand">
      <span class="cover-brand-name">Brandowave</span>
      <span class="cover-brand-dot"></span>
    </div>
    <p class="cover-tagline">EFFICIENCY THROUGH SIMPLICITY</p>
  </section>

  <section class="page next-page" aria-hidden="true"></section>

</main>
</body>
</html>
```